Website Revamp: Favorzo.com

Just got a new logo looking for a web design to go with the business. I need the photoshop files and stock photos. No Word Press Please.

```html
<!DOCTYPE html>
<html lang="en">
<head>
<meta charset="utf-8">
<title>Favorzo — Auto Recycling</title>
<link href="https://fonts.googleapis.com/css2?family=Roboto:wght@400;500;700;900&display=swap" rel="stylesheet">
<style>
:root{
  --green:#77bc3f;
  --green-bright:#7cc242;
  --black:#000;
  --grey-btn:#6b7475;
  --grey-dark:#5f6668;
  --text:#2b2b2b;
  --text-soft:#444;
  --footer-bg:#f2f2f2;
  --bar-bg:#6a6f72;
  --blue:#3aa0d8;
  --white:#fff;
}
*{margin:0;padding:0;box-sizing:border-box}
html,body{width:1200px;height:3574px;overflow:hidden;background:var(--white)}
body{font-family:'Roboto',sans-serif;color:var(--text)}
.page{position:relative;width:1200px;height:3574px;overflow:hidden}
.abs{position:absolute}
.center{left:0;width:1200px;text-align:center}

/* header */
.site-header{position:absolute;left:0;top:0;width:1200px;height:135px;background:var(--black)}
.brand{position:absolute;left:111px;top:48px;display:flex;align-items:center;gap:10px;color:var(--green);font-weight:700;font-size:26px}
.brand-dot{width:22px;height:22px;border-radius:50%;background:var(--green)}
.nav{position:absolute;top:62px;left:476px;display:flex;gap:0;font-size:13px;color:var(--white)}
.nav a{color:var(--white);text-decoration:none;position:absolute;white-space:nowrap}
.nav a.active{color:var(--green)}
.nav-underline{position:absolute;left:471px;top:131px;width:49px;height:4px;background:#555}
.quote-btn{position:absolute;left:967px;top:58px;width:122px;height:28px;background:var(--green);color:var(--white);font-size:12px;font-weight:700;display:flex;align-items:center;justify-content:center}

/* hero */
.hero{position:absolute;left:0;top:135px;width:1200px;height:633px;background:linear-gradient(180deg,#3d5f9a 0%,#5777a8 45%,#6b6470 70%,#7a5a5c 100%)}
.hero-ring{position:absolute;left:486px;top:80px;width:228px;height:228px;border-radius:50%;border:14px solid var(--green)}
.hero-title{position:absolute;left:0;width:1200px;top:350px;text-align:center;color:var(--white);font-size:72px;font-weight:900;letter-spacing:1px}
.hero-tag{position:absolute;left:416px;top:438px;width:368px;height:37px;background:#4d5357;clip-path:polygon(4% 0,96% 0,100% 100%,0 100%);color:var(--white);font-size:27px;font-weight:500;letter-spacing:5px;display:flex;align-items:center;justify-content:center}
.hero-btn{position:absolute;left:508px;top:497px;width:184px;height:59px;border-radius:30px;background:var(--green);color:var(--white);font-size:21px;font-weight:700;display:flex;align-items:center;justify-content:center}
.slider-dots{position:absolute;left:97px;top:245px}
.slider-dots span{display:block;width:14px;height:14px;border-radius:50%;background:#333;margin-bottom:12.5px}
.slider-dots span.on{background:var(--white)}

/* section titles */
.section-title{position:absolute;left:0;width:1200px;text-align:center;color:var(--green);font-size:47px;font-weight:700}
.pill{position:absolute;border-radius:30px;background:var(--grey-btn);color:var(--white);font-weight:700;display:flex;align-items:center;justify-content:center}

/* about */
.about-text{position:absolute;left:196px;width:808px;top:921px;text-align:center;font-size:18.5px;line-height:31px;color:var(--text)}

/* services */
.services{position:absolute;left:0;top:1204px;width:1200px;height:636px;background:linear-gradient(135deg,#d9d9d9 0%,#ececec 35%,#e3e3e3 60%,#d0d0d0 100%)}
.service{position:absolute;width:260px;text-align:center}
.service-icon{width:138px;height:138px;border-radius:50%;background:var(--white);margin:0 auto;display:flex;align-items:center;justify-content:center}
.service-icon.dark{background:var(--grey-dark)}
.service h3{font-size:22px;font-weight:500;color:#222;margin-top:20px}
.service p{font-size:12.5px;line-height:21px;color:#333;margin-top:13px}
.service .pill{position:relative;width:150px;height:46px;margin:22px auto 0;font-size:16px}

/* news */
.news-card{position:absolute;top:1989px;width:307px;text-align:center}
.news-thumb{width:307px;height:223px}
.news-card h4{font-size:17.5px;font-weight:500;line-height:28px;color:#222;margin-top:22px}
.news-card time{display:block;font-size:15.5px;color:#333;margin-top:8px}
.news-dots{position:absolute;top:2401px;left:578px;display:flex;gap:15px}
.news-dots span{width:12px;height:12px;border-radius:50%;background:var(--green)}
.news-dots span.on{background:#111}

/* contact */
.contact{position:absolute;left:0;top:2464px;width:1200px;height:678px;background:linear-gradient(180deg,#8cc63f 0%,#86c03f 50%,#7aaf3e 100%)}
.contact-title{position:absolute;left:0;width:1200px;top:100px;text-align:center;color:#2a2a2a;font-size:47px;font-weight:700}
.field{position:absolute;background:var(--white);font-size:17px;color:#333;padding:0 20px;display:flex;align-items:center}
.field.msg{align-items:flex-start;padding-top:18px;padding-left:30px}

/* footer */
.footer{position:absolute;left:0;top:3142px;width:1200px;height:381px;background:var(--footer-bg)}
.foot-col{position:absolute;top:68px}
.foot-col h5{font-size:22px;font-weight:500;color:#333}
.foot-about{font-size:14px;line-height:22px;color:#333;margin-top:28px;width:200px}
.foot-info{position:absolute;left:2px;display:flex;align-items:center;gap:14px;font-size:13.5px;font-weight:500;color:#222;white-space:nowrap}
.foot-list{list-style:none;margin-top:28px}
.foot-list li{display:flex;align-items:center;gap:14px;font-size:13.5px;font-weight:500;color:#222;height:33px}
.foot-list li.closed{color:var(--blue)}
.social{position:absolute;top:3452px;left:843px;display:flex;gap:43px}
.social span{width:16px;height:16px;border-radius:50%;background:#555}
.copyright{position:absolute;left:0;top:3523px;width:1200px;height:51px;background:var(--bar-bg);color:var(--white);font-size:13px;display:flex;align-items:center;justify-content:center}
</style>
</head>
<body>
<div class="page">

  <header class="site-header">
    <div class="brand"><span class="brand-dot"></span>Favorzo</div>
    <nav class="nav">
      <a class="active" style="left:0">HOME</a>
      <a style="left:76px">ABOUT US</a>
      <a style="left:164px">SERVICES</a>
      <a style="left:250px">LATEST NEWS</a>
      <a style="left:362px">CONTACT US</a>
    </nav>
    <div class="nav-underline"></div>
    <div class="quote-btn">GET A QUOTE</div>
  </header>

  <section class="hero" role="img" aria-label="Crushed cars stacked in a scrapyard under a blue sky">
    <div class="hero-ring"></div>
    <div class="hero-title">FAVORZO</div>
    <div class="hero-tag">AUTO RECYCLING</div>
    <div class="hero-btn">Read more</div>
    <div class="slider-dots"><span></span><span></span><span class="on"></span><span></span></div>
  </section>

  <h2 class="section-title" style="top:823px">ABOUT US</h2>
  <p class="about-text">Lorem ipsum dolor sit amet, consectetur adipiscing elit, sed do eiusmod tempor incididunt ut labore et dolore magna aliqua. Ut enim ad minim veniam, quis nostrud exercitation ullamco laboris nisi ut aliquip ex ea commodo consequat. Duis aute irure dolor in reprehenderit in voluptate velit esse cillum dolore eu fugiat nulla pariatur.</p>
  <div class="pill" style="left:508px;top:1083px;width:184px;height:58px;font-size:17px">READ MORE</div>

  <section class="services" role="img" aria-label="Faded close-up of engine parts and wheel hubs">
    <h2 class="section-title" style="top:47px">OUR SERVICES</h2>

    <div class="service" style="left:143px;top:165px">
      <div class="service-icon">
        <svg width="70" height="70" viewBox="0 0 70 70" fill="none" stroke="#77bc3f" stroke-width="3" stroke-linecap="round" stroke-linejoin="round">
          <path d="M12 58 L40 30"/><path d="M40 30 a11 11 0 1 0 8-16 l-6 6 -5-1 -1-5 6-6"/>
          <path d="M58 58 L30 30"/><path d="M30 30 L20 14 L14 20 Z"/><rect x="48" y="48" width="10" height="14" transform="rotate(-45 53 55)"/>
        </svg>
      </div>
      <h3>Excepteur sint</h3>
      <p>Lorem ipsum dolor sit amet, consectetur adipiscing elit, sed do eiusmod tempor incididunt ut labore et dolore magna aliqua. Ut enim ad minim veniam,</p>
      <div class="pill">Read more</div>
    </div>

    <div class="service" style="left:469px;top:165px">
      <div class="service-icon dark">
        <svg width="74" height="74" viewBox="0 0 74 74" fill="none" stroke="#fff" stroke-width="3" stroke-linecap="round" stroke-linejoin="round">
          <path d="M10 30 a28 28 0 0 1 50-10"/><path d="M60 12 v9 h-9"/>
          <path d="M64 44 a28 28 0 0 1 -50 10"/><path d="M14 62 v-9 h9"/>
          <path d="M18 44 l5-10 h28 l5 10 v8 h-38 z"/><circle cx="26" cy="52" r="4"/><circle cx="48" cy="52" r="4"/>
        </svg>
      </div>
      <h3>Lorium ipsum</h3>
      <p>Lorem ipsum dolor sit amet, consectetur adipiscing elit, sed do eiusmod tempor incididunt ut labore et dolore magna aliqua. Ut enim ad minim veniam,</p>
      <div class="pill">Read more</div>
    </div>

    <div class="service" style="left:806px;top:165px">
      <div class="service-icon">
        <svg width="72" height="72" viewBox="0 0 72 72" fill="none" stroke="#77bc3f" stroke-width="3" stroke-linejoin="round">
          <path d="M6 64 V24 L36 8 L66 24 V64 Z"/>
          <path d="M20 58 V44 l5-10 h22 l5 10 v14"/><path d="M20 50 h32"/>
          <circle cx="27" cy="52" r="2"/><circle cx="45" cy="52" r="2"/>
        </svg>
      </div>
      <h3>Duis aute irure</h3>
      <p>Lorem ipsum dolor sit amet, consectetur adipiscing elit, sed do eiusmod tempor incididunt ut labore et dolore magna aliqua. Ut enim ad minim veniam,</p>
      <div class="pill">Read more</div>
    </div>
  </section>

  <h2 class="section-title" style="top:1887px">LATEST NEWS</h2>

  <article class="news-card" style="left:122px">
    <div class="news-thumb" role="img" aria-label="Office team gathered around a laptop" style="background:linear-gradient(135deg,#d8d4cf,#b7a79a 50%,#e6e4e2)"></div>
    <h4>How to Build a Great Employee<br>Experience with...</h4>
    <time>July 1, 2019</time>
  </article>
  <article class="news-card" style="left:456px">
    <div class="news-thumb" role="img" aria-label="Keyboard with an orange customize key" style="background:linear-gradient(135deg,#3a3a3a,#6b5a3a 50%,#d98a1e 70%,#444)"></div>
    <h4>Migrating to Servora? Here<br>Are Top 4 Things...</h4>
    <time>May 5, 2018</time>
  </article>
  <article class="news-card" style="left:792px">
    <div class="news-thumb" role="img" aria-label="Hands typing on a laptop" style="background:linear-gradient(135deg,#eef1f3,#a9b3ba 55%,#3b4248)"></div>
    <h4>Highlights from Servora's<br>Harborline Release</h4>
    <time>January 11, 2018</time>
  </article>
  <div class="news-dots"><span></span><span class="on"></span><span></span></div>

  <section class="contact" role="img" aria-label="Green-tinted scrapyard road lined with old cars">
    <h2 class="contact-title">CONTACT US</h2>
    <div class="field" style="left:168px;top:193px;width:434px;height:49px">First Name</div>
    <div class="field" style="left:617px;top:193px;width:434px;height:49px">Last Name</div>
    <div class="field" style="left:168px;top:271px;width:434px;height:50px">Email</div>
    <div class="field" style="left:617px;top:271px;width:434px;height:50px">Phone</div>
    <div class="field msg" style="left:168px;top:350px;width:883px;height:140px">Message</div>
    <div class="pill" style="left:526px;top:532px;width:148px;height:46px;font-size:15px">SUBMIT</div>
  </section>

  <footer class="footer">
    <div class="foot-col" style="left:119px">
      <h5>Contact Us</h5>
      <p class="foot-about" style="margin-left:-3px">We are ipsum dolor sit amet aeeatt consectetuer adipiscing elitseder diam nonummy.</p>
    </div>
    <div class="foot-info" style="left:116px;top:216px">
      <svg width="12" height="14" viewBox="0 0 12 14" fill="none" stroke="#444" stroke-width="1.3"><path d="M6 13 C2 8 1 6 1 5 a5 5 0 0 1 10 0 c0 1-1 3-5 8z"/><circle cx="6" cy="5" r="1.6"/></svg>
      <span style="margin-left:4px">14 Ridge Lane, 3300 Millpark</span>
    </div>
    <div class="foot-info" style="left:114px;top:261px">
      <svg width="14" height="12" viewBox="0 0 14 12" fill="none" stroke="#444" stroke-width="1.3"><path d="M1 4 c2-3 10-3 12 0 l-2 2 -2-1 v-1 h-4 v1 l-2 1z"/><rect x="3" y="6" width="8" height="5"/></svg>
      <span style="margin-left:2px">+51234987</span>
    </div>
    <div class="foot-info" style="left:114px;top:305px">
      <svg width="14" height="10" viewBox="0 0 14 10" fill="none" stroke="#444" stroke-width="1.3"><rect x="1" y="1" width="12" height="8"/><path d="M1 1 l6 5 6-5"/></svg>
      <span style="margin-left:2px">hello@favorzo-mail.com</span>
    </div>

    <div class="foot-col" style="left:481px">
      <h5>Quick Links</h5>
      <ul class="foot-list" style="margin-left:2px">
        <li><svg width="7" height="12" viewBox="0 0 7 12"><path d="M1 1 l5 5 -5 5" fill="none" stroke="#555" stroke-width="1.3"/></svg>Home</li>
        <li><svg width="7" height="12" viewBox="0 0 7 12"><path d="M1 1 l5 5 -5 5" fill="none" stroke="#555" stroke-width="1.3"/></svg>About Us</li>
        <li><svg width="7" height="12" viewBox="0 0 7 12"><path d="M1 1 l5 5 -5 5" fill="none" stroke="#555" stroke-width="1.3"/></svg>Services</li>
        <li><svg width="7" height="12" viewBox="0 0 7 12"><path d="M1 1 l5 5 -5 5" fill="none" stroke="#555" stroke-width="1.3"/></svg>Latest News</li>
        <li><svg width="7" height="12" viewBox="0 0 7 12"><path d="M1 1 l5 5 -5 5" fill="none" stroke="#555" stroke-width="1.3"/></svg>Contact</li>
        <li><svg width="7" height="12" viewBox="0 0 7 12"><path d="M1 1 l5 5 -5 5" fill="none" stroke="#555" stroke-width="1.3"/></svg>24/7 Support</li>
      </ul>
    </div>

    <div class="foot-col" style="left:835px">
      <h5>Opening Hours</h5>
      <ul class="foot-list" style="margin-left:6px">
        <li><svg width="7" height="12" viewBox="0 0 7 12"><path d="M1 1 l5 5 -5 5" fill="none" stroke="#555" stroke-width="1.3"/></svg>Mon - Tue: 9.00 - 17.00</li>
        <li><svg width="7" height="12" viewBox="0 0 7 12"><path d="M1 1 l5 5 -5 5" fill="none" stroke="#555" stroke-width="1.3"/></svg>Wed - Thur: 9.00 - 16.00</li>
        <li><svg width="7" height="12" viewBox="0 0 7 12"><path d="M1 1 l5 5 -5 5" fill="none" stroke="#555" stroke-width="1.3"/></svg>Fri - Sat: 9.00 - 12.00</li>
        <li><svg width="7" height="12" viewBox="0 0 7 12"><path d="M1 1 l5 5 -5 5" fill="none" stroke="#555" stroke-width="1.3"/></svg>Saturday: 9.00 - 14.00</li>
        <li class="closed"><svg width="7" height="12" viewBox="0 0 7 12"><path d="M1 1 l5 5 -5 5" fill="none" stroke="#555" stroke-width="1.3"/></svg>Sunday: Closed</li>
      </ul>
    </div>
  </footer>
  <div class="social" aria-label="Social links"><span></span><span></span><span></span></div>

  <div class="copyright">Copyright @ 2020 www.favorzo-demo.com . All Rights Reserved</div>
</div>
</body>
</html>
```